Home Staging Company needs business card design

We're a home staging company called Brightwell Harbor Home Staging. We would like a business card design that includes aqua and gray. Our current logo of house within chair is fine but I find we almost always use the logo in one color. I'll upload images of front and back of our current card and our logo. Note that we have dropped "Solutions" from our company name and don't want to include it on the card.

Target Market(s)

Realtors and homeowners - people interested in selling their homes

Contact Information for Business Card

Marisol Fenwickley
Brightwell Harbor Home Staging
757-382-6190
www.brightwellharbor.com
marisol@brightwellharbor.com

Font styles to use
Serif
Script

Requirements
Must have
• My logo and contact details
• UPDATE***
• I forgot to say that the company name should be included on the front of the card somehow.

```html
<!DOCTYPE html>
<html lang="en">
<head>
<meta charset="utf-8">
<title>Brightwell Harbor Home Staging – Business Card</title>
<link rel="stylesheet" href="https://fonts.googleapis.com/css2?family=Playfair+Display:wght@400;700&display=swap">
<style>
  :root {
    --stage: #111111;
    --card-blue-light: #3ba3df;
    --card-blue-dark: #2a8fd0;
    --aqua: #5cc6c4;
    --charcoal-light: #3a3a3c;
    --charcoal-dark: #2b2b2d;
    --white: #ffffff;
    --brand-aqua: #5fc3cf;
  }
  * { box-sizing: border-box; margin: 0; padding: 0; }
  html, body {
    width: 1200px; height: 1000px; overflow: hidden;
    background: var(--stage);
  }
  .stage {
    position: relative; width: 1200px; height: 1000px;
  }
  .card {
    position: absolute; top: 357px;
    width: 500px; height: 286px;
    border-radius: 24px; overflow: hidden;
    box-shadow: 0 12px 30px rgba(0,0,0,.6);
  }
  .card-contact {
    left: 60px;
    background: linear-gradient(135deg, var(--card-blue-light), var(--card-blue-dark));
    color: var(--white);
    font-family: "Playfair Display", Georgia, serif;
    text-align: center;
  }
  .card-contact .edge-accents {
    position: absolute; inset: 0; width: 100%; height: 100%;
  }
  .contact-body {
    position: relative;
    display: flex; flex-direction: column; align-items: center;
    padding-top: 38px;
  }
  .brand-dot {
    width: 40px; height: 40px; border-radius: 50%;
    background: var(--white);
    margin-bottom: 8px;
  }
  .brand-small {
    font-size: 12px; letter-spacing: .5px; margin-bottom: 10px;
  }
  .person-name {
    font-size: 25px; font-weight: 400; letter-spacing: .3px;
  }
  .divider {
    width: 170px; height: 1px; background: var(--white);
    margin: 12px 0 14px;
  }
  .contact-line {
    font-size: 15px; line-height: 1.4;
  }
  .card-brand {
    left: 640px;
    background: linear-gradient(135deg, var(--charcoal-light), var(--charcoal-dark));
    display: flex; align-items: center; justify-content: center; gap: 16px;
  }
  .brand-mark {
    width: 46px; height: 46px; border-radius: 50%;
    background: var(--brand-aqua); flex: none;
  }
  .brand-name {
    font-family: "Playfair Display", Georgia, serif;
    font-weight: 400; font-size: 27px; line-height: 1.15;
    color: var(--brand-aqua);
  }
</style>
</head>
<body>
<main class="stage">
  <section class="card card-contact">
    <svg class="edge-accents" viewBox="0 0 500 286" preserveAspectRatio="none" aria-hidden="true">
      <polygon points="0,40 48,286 0,286" fill="var(--aqua)"/>
      <line x1="0" y1="22" x2="56" y2="286" stroke="var(--white)" stroke-width="4"/>
      <polygon points="500,246 452,0 500,0" fill="var(--aqua)"/>
      <line x1="500" y1="264" x2="444" y2="0" stroke="var(--white)" stroke-width="4"/>
    </svg>
    <div class="contact-body">
      <div class="brand-dot"></div>
      <p class="brand-small">Brightwell Harbor Home Staging</p>
      <h1 class="person-name">Marisol Fenwickley</h1>
      <div class="divider"></div>
      <p class="contact-line">757-382-6190</p>
      <p class="contact-line">www.brightwellharbor.com</p>
      <p class="contact-line">marisol@brightwellharbor.com</p>
    </div>
  </section>

  <section class="card card-brand">
    <div class="brand-mark"></div>
    <p class="brand-name">Brightwell Harbor<br>Home Staging</p>
  </section>
</main>
</body>
</html>
```